Holistic/ Sports Psychologist needs flyer design

I need a flyer designed that catches the attention of potential customers - (parents of young athletes and athletes) who may be looking for psychological services. I have a logo and all the relevant info for the flyer but would like someone to take it and make it look creative, fun, fresh and attention getting for high school and college athletes. The colors used can be from my logo design which represents my holistic approach.
Target Market(s)
high school and collegiate athletes
Industry/Entity Type
sports psychology
Requirements
Must have
- Info I put on the flyer with my logo and please add some graphics and color based on my logo

```html
<!DOCTYPE html>
<html lang="en">
<head>
<meta charset="utf-8">
<title>Holistic Psychology and Sports Psychology Consulting</title>
<link rel="stylesheet" href="https://fonts.googleapis.com/css2?family=Mali:wght@500;600;700&family=Roboto:ital,wght@0,400;0,500;0,700;1,500&display=swap">
<style>
  :root {
    --blue: #376a9e;
    --blue-light: #9ccbe6;
    --orange: #f2a430;
    --paper-top: #e9eff5;
    --paper-bottom: #ffffff;
    --ink: #1e1e1e;
    --ink-soft: #3c3c3c;
    --icon: #376a9e;
    --sand-light: #f4d9b7;
    --sand: #e2a862;
    --teal: #2f6d80;
    --teal-dark: #245766;
    --green: #a8cf6a;
    --cream: #fff6e6;
    --white: #ffffff;
    --rule: #d8e0e8;
  }
  html, body { margin: 0; padding: 0; overflow: hidden; background: #ffffff; }
  .flyer {
    position: relative; width: 942px; height: 1200px; overflow: hidden;
    background: linear-gradient(180deg, var(--paper-top) 0%, var(--paper-bottom) 75%);
    font-family: "Roboto", Arial, sans-serif; color: var(--ink);
  }
  .header-shape, .landscape { position: absolute; left: 0; top: 0; }
  .title {
    position: absolute; left: 0; top: 42px; width: 942px; margin: 0;
    text-align: center; color: var(--white);
    font-family: "Mali", cursive; font-weight: 700; font-size: 52px; line-height: 68px;
  }
  .services { position: absolute; left: 50px; top: 274px; width: 470px; }
  .services-heading {
    margin: 0 0 0 8px; font-style: italic; font-weight: 500; font-size: 22px;
    line-height: 29px; color: var(--ink-soft);
  }
  .service { position: absolute; left: 0; width: 470px; display: flex; }
  .service-icon { width: 46px; height: 46px; flex: none; margin-top: 2px; }
  .service-text {
    margin: 0 0 0 22px; font-size: 15.5px; line-height: 20px; color: var(--ink-soft);
  }
  .service-text strong { font-weight: 700; color: var(--ink); font-size: 16.5px; }
  .divider {
    position: absolute; left: 524px; top: 252px; width: 1px; height: 608px; background: var(--rule);
  }
  .profile { position: absolute; left: 580px; top: 270px; width: 340px; }
  .brand { display: flex; align-items: center; height: 72px; margin-left: -7px; }
  .brand-mark {
    width: 70px; height: 70px; border-radius: 50%; background: var(--blue); flex: none;
  }
  .brand-name {
    margin-left: 10px; font-size: 18px; font-weight: 400; color: var(--blue);
  }
  .bio { margin: 16px 0 0; font-size: 15.5px; line-height: 21px; }
  .bio strong { font-size: 19px; font-weight: 700; }
  .specialties-heading {
    margin: 18px 0 2px; font-style: italic; font-weight: 500; font-size: 20px;
  }
  .specialties { margin: 0; font-size: 15.5px; line-height: 21.5px; }
  .motto {
    position: absolute; left: 50px; top: 1043px; margin: 0;
    font-family: "Mali", cursive; font-weight: 600; font-size: 34px; line-height: 36px; color: var(--ink);
  }
  .motto-bar { position: absolute; left: 50px; top: 1162px; width: 181px; height: 8px; background: var(--green); }
  .contact {
    position: absolute; left: 547px; top: 980px; width: 295px; height: 220px;
    background: linear-gradient(180deg, rgba(150,110,60,0.55), rgba(70,70,70,0.75));
    text-align: center; color: var(--white);
  }
  .contact-lead {
    margin: 14px 0 12px; font-family: "Mali", cursive; font-weight: 600;
    font-size: 31px; line-height: 35px; color: var(--cream);
  }
  .contact-details { margin: 0; font-style: normal; font-weight: 500; font-size: 16.5px; line-height: 21.5px; }
</style>
</head>
<body>
<main class="flyer">
  <svg class="header-shape" width="942" height="320" viewBox="0 0 942 320" aria-hidden="true">
    <path d="M0 178 C120 222 260 236 400 230 L0 246 Z" fill="var(--orange)"/>
    <path d="M690 214 C820 222 905 255 942 318 V244 C880 222 790 212 690 214 Z" fill="var(--blue-light)"/>
    <path d="M0 0 H942 V246 C830 206 640 214 430 226 C260 236 110 222 0 178 Z" fill="var(--blue)"/>
  </svg>

  <h1 class="title">Holistic Psychology and<br>Sports Psychology Consulting</h1>

  <section class="services">
    <h2 class="services-heading">Ways to Improve Athletic Performance<br>Using Sports and Holistic Psychology</h2>

    <div class="service" style="top:100px">
      <svg class="service-icon" viewBox="0 0 46 46" aria-hidden="true">
        <path d="M24 4 C12 4 5 12 5 22 C5 28 8 31 9 34 V44 H27 V38 H32 C35 38 36 36 36 33 V28 L40 27 L36 20 C36 10 31 4 24 4 Z" fill="var(--icon)"/>
        <circle cx="20" cy="19" r="8" fill="none" stroke="#fff" stroke-width="2"/>
      </svg>
      <p class="service-text"><strong>Mental Skills Training – Ex:</strong><br>visualization, goal-setting, motivation, self- talk, mindset, concentration techniques.</p>
    </div>

    <div class="service" style="top:190px">
      <svg class="service-icon" viewBox="0 0 46 46" aria-hidden="true">
        <path d="M8 4 H30 L40 14 V42 H8 Z" fill="none" stroke="var(--icon)" stroke-width="3"/>
        <path d="M4 36 L16 26 L22 31 L34 20" fill="none" stroke="var(--icon)" stroke-width="3.5"/>
        <path d="M27 19 H35 V27" fill="none" stroke="var(--icon)" stroke-width="3.5"/>
      </svg>
      <p class="service-text"><strong>Performance Enhancement</strong> – eliminate psychological barriers that are hindering performance such as self- doubt, perfectionism, fear of failure, and burnout.</p>
    </div>

    <div class="service" style="top:296px">
      <svg class="service-icon" viewBox="0 0 46 46" aria-hidden="true">
        <path d="M24 4 C12 4 5 12 5 22 C5 28 8 31 9 34 V44 H27 V38 H32 C35 38 36 36 36 33 V28 L40 27 L36 20 C36 10 31 4 24 4 Z" fill="var(--icon)"/>
        <path d="M21 28 L13 20 C10 16 15 11 21 16 C27 11 32 16 29 20 Z" fill="#fff"/>
      </svg>
      <p class="service-text"><strong>Mental Health-</strong> anxiety and stress management by using things such as relaxation techniques, breathwork, and mindfulness practices.</p>
    </div>

    <div class="service" style="top:388px">
      <svg class="service-icon" viewBox="0 0 46 46" aria-hidden="true">
        <g fill="var(--icon)">
          <circle cx="8" cy="6" r="4"/><rect x="3" y="11" width="10" height="11" rx="3"/>
          <circle cx="23" cy="4" r="4"/><rect x="18" y="9" width="10" height="12" rx="3"/>
          <circle cx="38" cy="6" r="4"/><rect x="33" y="11" width="10" height="11" rx="3"/>
        </g>
        <path d="M10 25 L18 33 M36 25 L28 33" stroke="var(--icon)" stroke-width="2.5"/>
        <circle cx="23" cy="33" r="3.5" fill="none" stroke="var(--icon)" stroke-width="2.5"/>
        <rect x="18" y="38" width="10" height="7" rx="2" fill="none" stroke="var(--icon)" stroke-width="2.5"/>
      </svg>
      <p class="service-text"><strong>Injury Recovery Support-</strong> assist athletes in maintain resilience and positive mental attitude during rehabilitation as well as processing emotions relating to any potential trauma caused by the injury or life transitions resulting from it.</p>
    </div>

    <div class="service" style="top:520px">
      <svg class="service-icon" viewBox="0 0 46 46" aria-hidden="true">
        <polygon points="15,2 31,2 44,15 44,31 31,44 15,44 2,31 2,15" fill="var(--icon)"/>
        <circle cx="23" cy="23" r="13" fill="#fff"/>
        <path d="M17 17 L29 29 M29 17 L17 29" stroke="var(--icon)" stroke-width="4"/>
      </svg>
      <p class="service-text"><strong>Burnout prevention-</strong> teach athletes how to have balance in sports and life so they can experience longevity in their sports as well as overall optimal health and well-being.</p>
    </div>
  </section>

  <div class="divider"></div>

  <section class="profile">
    <div class="brand">
      <span class="brand-mark"></span>
      <span class="brand-name">Dr. Rosalind Hartwell</span>
    </div>
    <p class="bio"><strong>Dr. Rosalind Hartwell</strong> is a licensed psychologist. She understands the unique experiences of athletes due to her background as an All-American swimmer, collegiate and age group swim coach, parent of a collegiate/professional athlete, and sports psychology researcher. She works with athletes to optimize performance and overall well-being.</p>
    <h3 class="specialties-heading">Her specializations include:</h3>
    <p class="specialties">performance anxiety, mental performance, stress management, anxiety, depressions, trauma, life transitions, relationship issues, injury, and sleep.</p>
  </section>

  <svg class="landscape" width="942" height="1200" viewBox="0 0 942 1200" role="img" aria-label="Coastal landscape illustration with rolling sand hills, pine trees, a setting sun and an ocean wave">
    <defs>
      <linearGradient id="landscape-fill" x1="0" y1="0" x2="1" y2="0.35">
        <stop offset="0" stop-color="var(--sand-light)"/>
        <stop offset="0.45" stop-color="var(--sand)"/>
        <stop offset="1" stop-color="var(--teal)"/>
      </linearGradient>
    </defs>
    <path d="M0 912 C200 850 480 900 670 800 C740 730 860 700 942 700 V1200 H0 Z" fill="url(#landscape-fill)"/>
  </svg>

  <p class="motto">Be You<br>Be Love<br>Be Present</p>
  <div class="motto-bar"></div>

  <section class="contact">
    <p class="contact-lead">All services are<br>provided online</p>
    <address class="contact-details">2280 Harbor Lane #310<br>Cedar Point, FL 32099<br>904-555-0187<br>www.DrRosalindH.com</address>
  </section>
</main>
</body>
</html>
```